Sanding Disc Box Packaging Graphic design

We need a package design for 5" hook and loop sanding discs designed for use with random orbital sanders.

The Brand name is "BADGER BITE". Our brand stands for Quality, Strength and durability at an affordable price.
Sanding discs packaging, and tool packaging tends to be very functional and straightforward. We are looking for a package design that is creative and stands out while maintaining a serious and professional quality look. Identifying closely with our brand name is very important as well.

I've attached images of the product, and the image the branding was inspired from. A color palette based on those images would be nice but is not necessarily required. Please note however that our discs are yellow and not red.

We do not have our box template from our manufacturer yet but the dimensions of the box will be 127x127x74mm

Target Market(s)

We are aiming at a beginner to mid-level power tool user.

Industry/Entity Type

Power Tool

Font styles to use
Serif
Decorative

Colors

Designer to choose colors to be used in the design.

Requirements
Must have
• Our Brand name, Badger Bite must be on the box, preferably in a strong Bold font.
• We would also like our slogan somewhere on the box: "Designed for Strength, Built to Last"
• I've also attached an image showing the number of pieces of each grit sandpaper is in each box. We would like some similar indication on our packaging. Also an indication that these are 8 hole sanding discs is needed as well.
Nice to have
• The packaging may also be used for other sanding products such as sanding belts, sponges, etc as the line expands so versatility is a plus. A vector design is preferred.
• A space on the back of the package for a more detailed product description with a matching font would helpful. The copy hasn't been written yet but the description will around 100 words. Placeholder text would be fine.
Should not have
• Absolutely DO NOT use images from other artists within your design. If this is done you will not win this design contest. I
• Also, please do not use the attached gorilla image in your designs. We have tried to locate the copyright holder to obtain printing rights but haven't been successful.
• Also, please stay away from the aesthetic of the product "Falcon paste". For trademark purposes the design needs to be as distinct from that product logo and packaging as possible.

```html
<!DOCTYPE html>
<html lang="en">
<head>
<meta charset="utf-8">
<title>Badger Bite – Sanding Disc Box</title>
<link rel="stylesheet" href="https://fonts.googleapis.com/css2?family=League+Gothic&family=Antonio:wght@300;700&display=swap">
<style>
  :root {
    --stage: #e4e4e4;
    --box-black: #1f1f1f;
    --brand-gold: #b9ad52;
    --ink-grey: #d3d3d3;
    --body-grey: #a9a9a9;
    --hole-dark: #1f1f1f;
  }
  * { margin: 0; padding: 0; box-sizing: border-box; }
  html, body { width: 1200px; height: 1000px; overflow: hidden; }
  body { background: var(--stage); position: relative; }

  .panel { position: absolute; background: var(--box-black); top: 120px; height: 760px; overflow: hidden; }
  .side-panel { left: 60px; width: 360px; }
  .front-panel { left: 420px; width: 720px; border-left: 1px solid #2c2c2c; }

  /* side panel */
  .side-heading {
    position: absolute; left: 22px; top: 20px;
    font-family: "League Gothic", "Arial Narrow", sans-serif; font-weight: 400;
    font-size: 28px; letter-spacing: 0.5px; color: var(--brand-gold);
    white-space: nowrap;
  }
  .product-copy {
    position: absolute; left: 22px; top: 72px; width: 200px;
    font-family: "Antonio", "Arial Narrow", sans-serif; font-weight: 300;
    font-size: 12px; line-height: 1.6; text-transform: uppercase;
    color: var(--body-grey);
  }
  .grit-list {
    position: absolute; right: 22px; top: 72px; width: 100px;
    list-style: none; text-align: center;
    font-family: "League Gothic", "Arial Narrow", sans-serif;
    color: var(--ink-grey);
  }
  .grit-item { margin-bottom: 26px; line-height: 0.95; }
  .grit-count { display: block; font-size: 44px; }
  .grit-number { display: block; font-size: 58px; }
  .grit-label { display: block; font-size: 40px; }
  .disc-size {
    position: absolute; right: 44px; bottom: 16px;
    font-family: "League Gothic", "Arial Narrow", sans-serif;
    font-size: 72px; color: var(--ink-grey); line-height: 1;
  }
  .side-mascot {
    position: absolute; left: 22px; bottom: 22px; width: 190px; height: 220px;
    background: radial-gradient(ellipse at 50% 45%, #b9ad52 0%, #6f6834 60%, #2a2a22 100%);
    border-radius: 8px;
  }

  /* front panel */
  .front-mascot {
    position: absolute; left: 100px; top: 140px; width: 250px; height: 520px;
    background: radial-gradient(ellipse at 50% 40%, #e6e6e6 0%, #9b9b9b 55%, #3a3a3a 100%);
    border-radius: 40% 40% 30% 30%;
  }
  .text-column {
    position: absolute; left: 385px; top: 22px; width: 310px;
    text-align: center; white-space: nowrap;
  }
  .brand-name {
    font-family: "League Gothic", "Arial Narrow", sans-serif; font-weight: 400;
    color: var(--brand-gold); line-height: 0.9;
  }
  .brand-line-one { display: block; font-size: 128px; letter-spacing: 1px; }
  .brand-line-two { display: block; font-size: 196px; letter-spacing: 2px; }
  .slogan { font-family: "Antonio", "Arial Narrow", sans-serif; color: var(--ink-grey); line-height: 1.05; margin-top: 12px; }
  .slogan-lead { display: block; font-weight: 300; font-size: 64px; }
  .slogan-mid { display: block; font-weight: 300; font-size: 40px; margin-top: 2px; }
  .slogan-end { display: block; font-weight: 700; font-size: 44px; margin-top: 10px; }
  .disc-row { position: absolute; left: 395px; top: 630px; width: 290px; height: 68px; }
</style>
</head>
<body>
  <section class="panel side-panel">
    <h2 class="side-heading">HOOK AND LOOP SANDING DISCS</h2>
    <p class="product-copy">Premium 5 inch hook and loop discs with eight holes for fast dust pickup on random orbital sanders. Tough aluminum oxide grit cuts clean and lasts longer on wood, paint, metal and filler. Start with 80 grit for shaping, move to 120 for smoothing and finish with 220 for a fine surface ready for stain or paint.</p>
    <ul class="grit-list">
      <li class="grit-item"><span class="grit-count">20X</span><span class="grit-number">80</span><span class="grit-label">GRIT</span></li>
      <li class="grit-item"><span class="grit-count">20X</span><span class="grit-number">120</span><span class="grit-label">GRIT</span></li>
      <li class="grit-item"><span class="grit-count">20X</span><span class="grit-number">220</span><span class="grit-label">GRIT</span></li>
    </ul>
    <div class="side-mascot" role="img" aria-label="Gold illustration of the crouching brand mascot animal"></div>
    <div class="disc-size">5"</div>
  </section>

  <section class="panel front-panel">
    <div class="front-mascot" role="img" aria-label="Large grey line illustration of the roaring brand mascot animal head"></div>
    <div class="text-column">
      <h1 class="brand-name"><span class="brand-line-one">BADGER</span><span class="brand-line-two">BITE</span></h1>
      <p class="slogan">
        <span class="slogan-lead">DESIGNED</span>
        <span class="slogan-mid">FOR STRENGTH</span>
        <span class="slogan-end">BUILT TO LAST</span>
      </p>
    </div>
    <svg class="disc-row" viewBox="0 0 290 68" aria-label="Four 8-hole sanding discs">
      <defs>
        <g id="disc">
          <circle r="31" fill="#b9ad52"/>
          <g fill="#1f1f1f">
            <circle cx="0" cy="-19" r="2.8"/><circle cx="13.4" cy="-13.4" r="2.8"/>
            <circle cx="19" cy="0" r="2.8"/><circle cx="13.4" cy="13.4" r="2.8"/>
            <circle cx="0" cy="19" r="2.8"/><circle cx="-13.4" cy="13.4" r="2.8"/>
            <circle cx="-19" cy="0" r="2.8"/><circle cx="-13.4" cy="-13.4" r="2.8"/>
          </g>
        </g>
      </defs>
      <use href="#disc" x="33" y="34"/>
      <use href="#disc" x="108" y="34"/>
      <use href="#disc" x="183" y="34"/>
      <use href="#disc" x="257" y="34"/>
    </svg>
  </section>
</body>
</html>
```